Speisekarte Heuriger
Zielgruppe
Wir sind ein Gastronomielokal im Burgenland. Ein Heuriger ist ein traditionelles Lokal in dem hauptsächlich kalte und einfache warme Speisen verabreicht werden. (Brote, kaltes und warmes gebratenes Fleisch, gemischte Teller, Strudl usw.) Aber ein großer Schwerpunkt liegt dabei auch immer auf den eigenen Weinen.
Aufgabenstellung
Da ein Heuriger aus dem Weinbau und somit Landwirtschaft kommt bevorzuge ich eher ein schlichtes traditionelles Design. Ein grüner Farbbereich ist vielleicht das Beste. (nicht stechend grün. eher hell) (Vielleicht im Internet nach Speisekarte Heuriger/Buschenschank suchen)
Ich benötige eine Vorlage für die Speisekarte in Indesign am besten erstellt mit dem drukwelle.at plugin damit die Größen passen.
Speisekarte mit Umschlag 8 Innenseiten mit 4seitigem Umschlag haben.
In A5 hoch
CMYK-Farbmodell
Klammerheftung
Umschlag:
Vorderseite natürlich mit "Speisekarte" drauf mit Logo, Und evtl der Name: "Heuriger Familie Pelkinger" usw.
die vordere Innenseite kann leer sein. Evtl auch gesamte Anschrift hier rein. Oder auch auf die Rückseite. Das ist freigestellt.
Auf der hinteren Innenseite muss die Allergenverordnung mit den Allergenen und dazugehörigen Buchstaben vorhanden sein! (Achtung für Österreich! Gibt genug Beispielbilder im Internet)
Auf der Rückseite hinten sollte stehen: "Wir bedanken uns für Ihren Besuch und freuen uns darauf, Sie bald wieder bei uns begrüßen zu dürfen!
Familie Pelkinger" (Natürlich nicht in einer Wurst)
Innenseiten: (Text schreibe ich selber. Aber vielleicht ein paar Beispiele für Schriftart und Größe/Farbe)
Erste Seite (rechts): Getränke
Zweite Seite: Kalte Speisen
Dritte Seite: Brote
Vierte Seite: Warme Speisen
Fünfte Seite: Beilagen/Salate
Sechste Seite: Für unsere kleinen Gäste/ Strudel
Siebente Seite: Weißwein
Achte Seite: Rotwein
Die Seitenbelegung ist nur als Info gedacht. Ich habe leider keine schönen Fotos von den Speisen gemacht und will auch keine fremden Speisen in meiner Karte sehen. Also keine Speisebilder. (Mit Ausnahme von Weintrauben vielleicht. Bezug zum Weinbau usw.)
Anbei habe ich die Logos von unseren Etiketten. Man kann das P auch alleine ohne dem Namen darunt..

```html
<!DOCTYPE html>
<html lang="de">
<head>
<meta charset="utf-8">
<title>Speisekarte – Heuriger Familie Pelkinger</title>
<link href="https://fonts.googleapis.com/css2?family=Montserrat:wght@400;500;600&display=swap" rel="stylesheet">
<style>
  :root {
    --stage: #262626;
    --paper-light: #e4e4e4;
    --paper-mid: #c9c9c9;
    --paper-dark: #b3b3b3;
    --brand-green: #3b9440;
    --ink: #1e1e1e;
    --ink-soft: #3a3a3a;
    --rule: #6e6e6e;
  }
  * { box-sizing: border-box; margin: 0; padding: 0; }
  html, body {
    width: 1200px; height: 675px; overflow: hidden;
    background: var(--stage);
    font-family: "Montserrat", sans-serif;
    color: var(--ink);
  }
  .spread { position: relative; width: 1200px; height: 675px; }
  .page {
    position: absolute; top: 76px; width: 368px; height: 524px;
    overflow: hidden;
  }
  .page--cover { left: 34px; }
  .page--cold { left: 416px; }
  .page--bread { left: 798px; }
  .page__texture {
    position: absolute; inset: 0;
    background:
      radial-gradient(ellipse at 30% 20%, var(--paper-light) 0%, transparent 55%),
      radial-gradient(ellipse at 75% 80%, var(--paper-light) 0%, transparent 50%),
      linear-gradient(160deg, var(--paper-mid) 0%, var(--paper-dark) 50%, var(--paper-mid) 100%);
  }

  /* Cover */
  .cover__mark {
    position: absolute; left: 124px; top: 69px;
    width: 121px; height: 121px; border-radius: 7px;
    background: var(--brand-green);
  }
  .cover__name {
    position: absolute; left: 124px; top: 198px; width: 121px;
    text-align: center; color: var(--brand-green);
    font-size: 11px; font-weight: 500; letter-spacing: 3px;
  }
  .cover__title {
    position: absolute; left: 69px; top: 314px; width: 262px;
    text-align: center; font-size: 19px; font-weight: 400;
    letter-spacing: 5.4px; color: var(--ink);
  }
  .cover__subtitle {
    position: absolute; left: 69px; top: 341px; width: 262px;
    text-align: center; font-size: 10px; font-weight: 500;
    letter-spacing: 0.6px; color: var(--ink-soft);
  }

  /* Inner pages */
  .page__mark {
    position: absolute; left: 155px; top: 24px;
    width: 58px; height: 58px; border-radius: 5px;
    background: var(--brand-green);
  }
  .page__brand {
    position: absolute; left: 0; right: 0; top: 87px;
    text-align: center; color: var(--brand-green);
    font-size: 7px; font-weight: 500; letter-spacing: 2px;
  }
  .page__heading {
    position: absolute; left: 0; right: 0; top: 105px;
    text-align: center; font-size: 11px; font-weight: 500;
    letter-spacing: 1px; text-shadow: 0 3px 4px rgba(0,0,0,0.25);
  }
  .menu {
    position: absolute; left: 39px; right: 39px; top: 155px;
    list-style: none;
  }
  .menu__item {
    padding: 4px 0 4px;
    border-bottom: 1px solid var(--rule);
  }
  .menu__item:last-child { border-bottom: none; }
  .menu__head {
    display: flex; justify-content: space-between; align-items: baseline;
    font-size: 8px; font-weight: 600; letter-spacing: 0.4px; line-height: 10px;
  }
  .menu__desc {
    font-size: 6.4px; line-height: 8.5px; color: var(--ink-soft);
    max-width: 200px;
  }
  .menu__allergens {
    font-size: 5px; line-height: 8px; color: var(--ink-soft);
  }
</style>
</head>
<body>
<main class="spread">

  <section class="page page--cover">
    <div class="page__texture" role="img" aria-label="Hellgraue Eisblumen-Struktur als Papierhintergrund"></div>
    <div class="cover__mark"></div>
    <div class="cover__name">PELKINGER</div>
    <h1 class="cover__title">SPEISEKARTE</h1>
    <p class="cover__subtitle">HEURIGER | FAMILIE PELKINGER</p>
  </section>

  <section class="page page--cold">
    <div class="page__texture" role="img" aria-label="Hellgraue Eisblumen-Struktur als Papierhintergrund"></div>
    <div class="page__mark"></div>
    <div class="page__brand">PELKINGER</div>
    <h2 class="page__heading">KALTE SPEISEN</h2>
    <ul class="menu">
      <li class="menu__item"><div class="menu__head"><span>HAUSPLATTE</span><span>5,50 €</span></div><p class="menu__desc">Sur-, Kümmelbraten, Geselchtes, Presswurst und Blunze, garniert, inkl. Brot</p><p class="menu__allergens">AB*</p></li>
      <li class="menu__item"><div class="menu__head"><span>LUFTGETROCKNETER ROHSCHINKEN</span><span>6,00 €</span></div><p class="menu__desc">mit Zuckermelone, garniert, inkl. Brot</p><p class="menu__allergens">AB*</p></li>
      <li class="menu__item"><div class="menu__head"><span>SURBRATEN</span><span>5,00 €</span></div><p class="menu__desc">garniert, inkl. Brot</p><p class="menu__allergens">AB*</p></li>
      <li class="menu__item"><div class="menu__head"><span>GESELCHTES</span><span>5,00 €</span></div><p class="menu__desc">garniert, inkl. Brot</p><p class="menu__allergens">AB*</p></li>
      <li class="menu__item"><div class="menu__head"><span>KÜMMELBRATEN</span><span>5,00 €</span></div><p class="menu__desc">garniert, inkl. Brot</p><p class="menu__allergens">AB*</p></li>
      <li class="menu__item"><div class="menu__head"><span>PRESSWURST MIT ZWIEBEL</span><span>4,00 €</span></div><p class="menu__desc">inkl. Brot, auf Wunsch mit Kernöl</p><p class="menu__allergens">AB*</p></li>
      <li class="menu__item"><div class="menu__head"><span>SAURE WURST MIT ZWIEBEL</span><span>4,00 €</span></div><p class="menu__desc">inkl. Brot, auf Wunsch mit Kernöl</p><p class="menu__allergens">AB*</p></li>
      <li class="menu__item"><div class="menu__head"><span>KÄSESTANGERL</span><span>2,00 €</span></div><p class="menu__desc">mit Gouda</p><p class="menu__allergens">AB*</p></li>
    </ul>
  </section>

  <section class="page page--bread">
    <div class="page__texture" role="img" aria-label="Hellgraue Eisblumen-Struktur als Papierhintergrund"></div>
    <div class="page__mark"></div>
    <div class="page__brand">PELKINGER</div>
    <h2 class="page__heading">BROTE</h2>
    <ul class="menu">
      <li class="menu__item"><div class="menu__head"><span>BELEGTES HAUSBROT</span><span>4,00 €</span></div><p class="menu__desc">mit Sur- und Kümmelbraten, Geselchtem und Presswurst, garniert</p><p class="menu__allergens">AB*</p></li>
      <li class="menu__item"><div class="menu__head"><span>SCHINKENBROT</span><span>3,50 €</span></div><p class="menu__desc">mit Gurkerl</p><p class="menu__allergens">AB*</p></li>
      <li class="menu__item"><div class="menu__head"><span>SURBRATENBROT</span><span>3,50 €</span></div><p class="menu__desc">mit Gurkerl</p><p class="menu__allergens">AB*</p></li>
      <li class="menu__item"><div class="menu__head"><span>KÜMMELBRATENBROT</span><span>3,50 €</span></div><p class="menu__desc">mit Gurkerl</p><p class="menu__allergens">AB*</p></li>
      <li class="menu__item"><div class="menu__head"><span>WURSTBROT</span><span>2,50 €</span></div><p class="menu__desc">mit Extrawurst</p><p class="menu__allergens">AB*</p></li>
      <li class="menu__item"><div class="menu__head"><span>KÄSEBROT</span><span>2,50 €</span></div><p class="menu__desc">mit Gouda</p><p class="menu__allergens">AB*</p></li>
      <li class="menu__item"><div class="menu__head"><span>PASTETENBROT</span><span>2,50 €</span></div><p class="menu__desc">hausgemacht</p><p class="menu__allergens">AB*</p></li>
      <li class="menu__item"><div class="menu__head"><span>PASTETENBROT MIT PFEFFERONI</span><span>2,50 €</span></div><p class="menu__desc">hausgemacht</p><p class="menu__allergens">AB*</p></li>
    </ul>
  </section>

</main>
</body>
</html>
```